Photography Studio Prep Guide Design Needed

I have a prep guide I send to all parents who book a session - It is outdated and ugly. I want a gorgeous, clean, modern upscale look for the brochure I send.

I already have the text and can provide photos for the final design. I want the cover to be clean and upscale and modern, with a happy feel.

Target Market(s)

My clients for an upscale Newborn Photography Studio

Requirements
Must have
• space for my photos, an upscale clean feel
Nice to have
• I love color, but don't want the brochure to look busy. I love cream, white, pale pink.

```html
<!DOCTYPE html>
<html lang="en">
<head>
<meta charset="utf-8">
<title>Newborn Session Prep Guide – Page 2</title>
<link href="https://fonts.googleapis.com/css2?family=Italianno&family=Lora:ital,wght@1,600&display=swap" rel="stylesheet">
<style>
  :root {
    --blush: #efb8bc;
    --blush-deep: #e3a4a9;
    --bow-pink: #deaaac;
    --paper: #ffffff;
    --grass-dark: #2c5a2e;
    --grass-mid: #3f7a3c;
    --grass-light: #4f8a48;
    --stitch: #c9c9c9;
    --ink-light: #ffffff;
  }
  * { margin: 0; padding: 0; box-sizing: border-box; }
  html, body {
    width: 1179px; height: 1200px; overflow: hidden;
    background: var(--blush);
  }
  .page {
    position: relative; width: 1179px; height: 1200px;
    background: var(--blush);
  }
  .page__frame {
    position: absolute; left: 16px; top: 20px; width: 1147px; height: 1160px;
    background: var(--paper); border-radius: 10px; padding: 4px;
  }
  .page__field {
    position: absolute; inset: 4px; border-radius: 8px;
    background:
      radial-gradient(ellipse at 30% 20%, var(--grass-light) 0%, transparent 55%),
      radial-gradient(ellipse at 75% 70%, var(--grass-light) 0%, transparent 50%),
      linear-gradient(160deg, var(--grass-mid), var(--grass-dark) 60%, var(--grass-mid));
  }
  .page__stitch {
    position: absolute; left: 36px; top: 42px; width: 1107px; height: 1118px;
    border: 2px dashed var(--stitch); border-radius: 10px;
  }
  .tip {
    position: absolute; left: 40px; width: 1099px; text-align: center;
    color: var(--ink-light);
  }
  .tip__title {
    display: inline-block;
    font-family: "Italianno", cursive;
    font-weight: 400; font-size: 44px; line-height: 40px;
    padding: 0 2px 2px;
    border-bottom: 2px solid var(--blush);
  }
  .tip__body {
    margin-top: 12px;
    font-family: "Lora", Georgia, serif;
    font-style: italic; font-weight: 600;
    font-size: 17.6px; line-height: 26.4px;
    letter-spacing: 0.2px; white-space: nowrap;
  }
  .tip--awake { top: 70px; }
  .tip--clothes { top: 278px; }
  .tip--pacifier { top: 436px; }
  .tip--pacifier .tip__body { margin-top: 22px; }

  .photo-slot {
    position: absolute; top: 648px; width: 481px; height: 478px;
    background: var(--paper); border-radius: 8px;
  }
  .photo-slot::after {
    content: ""; position: absolute; inset: 12px;
    border: 1.5px dashed var(--blush-deep);
  }
  .photo-slot--left { left: 61px; }
  .photo-slot--right { left: 640px; }
  .photo-slot__bow {
    position: absolute; top: -20px; width: 112px; height: 110px; z-index: 2;
  }
  .photo-slot--left .photo-slot__bow { left: 186px; }
  .photo-slot--right .photo-slot__bow { left: 186px; }
</style>
</head>
<body>
<main class="page">
  <div class="page__frame">
    <div class="page__field" role="img" aria-label="Lush green grass background"></div>
  </div>
  <div class="page__stitch"></div>

  <section class="tip tip--awake">
    <h2 class="tip__title">3. Keep baby awake</h2>
    <p class="tip__body">Interact with, and keep baby awake for 2 hours preceding your appointment to make sure they<br>
    are nice and sleepy for their session. A great way to do this is by giving baby a bath – which will get<br>
    them nice and clean and keep them awake. Also – keeping baby naked, in a diaper only is a good way<br>
    to keep them awake and alert. This step is extremely important – otherwise it can take a long time to get<br>
    baby to sleep, and we will have less time for photos.</p>
  </section>

  <section class="tip tip--clothes">
    <h2 class="tip__title">4. Clothes</h2>
    <p class="tip__body">Please dress baby in a simple loose sleeper we can just unsnap when you arrive – we want to<br>
    keep baby as calm and happy as possible and want to avoid clothes we have to pull over their head.<br>
    I provide all clothing/hats/props at your session.</p>
  </section>

  <section class="tip tip--pacifier">
    <h2 class="tip__title">5. Pacifier</h2>
    <p class="tip__body">Please bring a pacifier – it can be very helpful during a session if a baby is fussy. Please note I only<br>
    use the pacifier for a few minutes at a time to soothe into a pose. If you choose not to bring a pacifier I<br>
    will respect your decision, but please understand we may have to pass on several poses if you do not<br>
    bring one.</p>
  </section>

  <div class="photo-slot photo-slot--left" aria-label="Photo space">
    <svg class="photo-slot__bow" viewBox="0 0 112 110" role="img" aria-label="Pale pink ribbon bow ornament">
      <rect x="0" y="0" width="112" height="110" rx="20" fill="var(--bow-pink)" opacity="0.9"/>
    </svg>
  </div>
  <div class="photo-slot photo-slot--right" aria-label="Photo space">
    <svg class="photo-slot__bow" viewBox="0 0 112 110" role="img" aria-label="Pale pink ribbon bow ornament">
      <rect x="0" y="0" width="112" height="110" rx="20" fill="var(--bow-pink)" opacity="0.9"/>
    </svg>
  </div>
</main>
</body>
</html>
```